Geothermal company needs a creative "POW" business card

Manufacturers tend to be boring. We are not! We are a Geothermal Heat Pump company that has over 30 yrs of experience and wants a new look and updated feel. Nothing old (yawn) so get your creative hats on and let's rock!

We want to use the great colors of lime green and navy blue. Our new logo is attached and we're ready to roll. Remember, we're a professional leader in the geothermal industry that needs to make an eye catching and memorable first glance.

```html
<!DOCTYPE html>
<html lang="en">
<head>
<meta charset="utf-8">
<title>Boreal Terra – Business Card</title>
<link rel="stylesheet" href="https://fonts.googleapis.com/css2?family=Open+Sans:wght@400;600;700&display=swap">
<style>
  :root {
    --lime: #7cc242;
    --lime-light: #8fd04a;
    --green-deep: #1e8a2e;
    --navy: #1b3a8c;
    --ink: #555b61;
    --divider: #c9ccd0;
    --paper: #ffffff;
    --backdrop: #eceeef;
  }
  * { margin: 0; padding: 0; box-sizing: border-box; }
  html, body { width: 1200px; height: 720px; overflow: hidden; }
  body {
    background: var(--backdrop);
    font-family: "Open Sans", Arial, sans-serif;
    position: relative;
  }
  .card {
    position: absolute;
    top: 205px;
    width: 540px;
    height: 309px;
    border-radius: 4px;
    box-shadow: 0 6px 18px rgba(0,0,0,0.14);
    overflow: hidden;
  }
  .card--front { left: 40px; background: var(--paper); }
  .card--back {
    left: 620px;
    background: linear-gradient(160deg, var(--green-deep) 0%, #3da338 55%, var(--lime-light) 100%);
  }

  /* Front */
  .brand { position: absolute; left: 34px; top: 34px; display: flex; align-items: center; gap: 16px; }
  .brand__dot { width: 72px; height: 72px; border-radius: 50%; background: var(--navy); flex: none; }
  .brand__name { font-size: 44px; font-weight: 700; color: var(--lime); line-height: 1; letter-spacing: -0.5px; }
  .brand__tagline { margin-top: 4px; font-size: 12.5px; font-weight: 700; color: var(--navy); white-space: nowrap; }

  .person {
    position: absolute; right: 296px; top: 166px; text-align: right;
  }
  .person__name { font-size: 21px; font-weight: 600; color: var(--lime); line-height: 1.1; }
  .person__title { font-size: 13px; color: var(--ink); margin-top: 2px; }
  .person__address { font-size: 13px; color: var(--ink); margin-top: 14px; line-height: 1.45; }

  .divider { position: absolute; left: 262px; top: 160px; width: 1px; height: 112px; background: var(--divider); }

  .contacts { position: absolute; left: 278px; top: 160px; list-style: none; }
  .contacts li { display: flex; align-items: center; gap: 9px; font-size: 13.5px; color: var(--ink); height: 26px; }
  .contacts svg { width: 16px; height: 16px; flex: none; }

  /* Back */
  .back-mark { position: absolute; left: 0; right: 0; top: 56px; display: flex; flex-direction: column; align-items: center; gap: 14px; }
  .back-mark__dot { width: 120px; height: 120px; border-radius: 50%; background: var(--navy); }
  .back-mark__name { font-size: 30px; font-weight: 700; color: var(--paper); line-height: 1; }
  .back-url { position: absolute; left: 0; right: 0; bottom: 34px; text-align: center; color: var(--paper); font-size: 17px; letter-spacing: 2px; }
</style>
</head>
<body>
  <section class="card card--front" aria-label="Business card front">
    <div class="brand">
      <span class="brand__dot"></span>
      <div>
        <div class="brand__name">Boreal Terra</div>
        <div class="brand__tagline">Builders of Ground-Source Heating Systems Since 1990</div>
      </div>
    </div>

    <div class="person">
      <div class="person__name">Your Name</div>
      <div class="person__title">CEO</div>
      <div class="person__address">218 Cedar Ridge Rd<br>Lakeview, MN 55090</div>
    </div>

    <span class="divider"></span>

    <ul class="contacts">
      <li>
        <svg viewBox="0 0 16 16" aria-hidden="true"><circle cx="8" cy="8" r="8" fill="var(--lime)"/><path d="M5.4 4.2l1.4 1.6-.8 1c.5 1 1.3 1.9 2.3 2.4l1-.8 1.6 1.4-.8 1.3c-2.9-.5-5.2-2.8-5.7-5.7z" fill="#fff"/></svg>
        (555) 014-2200
      </li>
      <li>
        <svg viewBox="0 0 16 16" aria-hidden="true"><circle cx="8" cy="8" r="8" fill="var(--lime)"/><rect x="5.5" y="3.5" width="5" height="9" rx="1" fill="#fff"/><rect x="6.5" y="4.8" width="3" height="5.4" fill="var(--lime)"/></svg>
        (555) 014-2201
      </li>
      <li>
        <svg viewBox="0 0 16 16" aria-hidden="true"><circle cx="8" cy="8" r="8" fill="var(--lime)"/><rect x="4" y="5" width="8" height="6" rx="0.8" fill="#fff"/><path d="M4.3 5.4L8 8.3l3.7-2.9" stroke="var(--lime)" stroke-width="1" fill="none"/></svg>
        yourname@borealterra.com
      </li>
      <li>
        <svg viewBox="0 0 16 16" aria-hidden="true"><circle cx="8" cy="8" r="8" fill="var(--lime)"/><circle cx="8" cy="8" r="4.2" fill="none" stroke="#fff" stroke-width="1"/><ellipse cx="8" cy="8" rx="1.8" ry="4.2" fill="none" stroke="#fff" stroke-width="1"/><path d="M3.8 8h8.4" stroke="#fff" stroke-width="1"/></svg>
        www.borealterra.com
      </li>
    </ul>
  </section>

  <section class="card card--back" aria-label="Business card back">
    <div class="back-mark">
      <span class="back-mark__dot"></span>
      <span class="back-mark__name">Boreal Terra</span>
    </div>
    <div class="back-url">www.borealterra.com</div>
  </section>
</body>
</html>
```